Project, Programme and Portfolio Management Consultant needs a business card

I have recently had someone create a brand guide for me and I wish to have new business cards that incorporate the new brand. I am an independent management consultant working with businesses to improve their ability to deliver their business strategy through selecting the right project, the right people and doing it in the right way. Whilst I am currently working on my own, I am hoping to start to build win business where I need to bring in a team and this branding activity is the start of that process.

Target Market(s)

Medium to large businesses, government departments and defence

Contact Information for Business Card

Name
job title
business name
mobile
email
website
linkedIn profile

Font styles to use
Other font styles liked:
• roboto light

Colors

Designer to choose colors to be used in the design.

Requirements
Must have
• Must use my logo and brand colours (see attached brand guide)

```html
<!DOCTYPE html>
<html lang="en">
<head>
<meta charset="utf-8">
<title>Verantis business card</title>
<link href="https://fonts.googleapis.com/css2?family=Montserrat:wght@400;500;600&display=swap" rel="stylesheet">
<style>
  :root {
    --backdrop: #9a9a9a;
    --navy: #1a1e38;
    --deep-blue: #0f3c6b;
    --teal: #06aeaa;
    --gold: #e0aa1a;
    --ink: #4a4a4a;
    --paper: #ffffff;
  }
  * { margin: 0; padding: 0; box-sizing: border-box; }
  html, body { width: 1200px; height: 930px; overflow: hidden; }
  body {
    background: radial-gradient(circle at 45% 45%, #b9b9b9, var(--backdrop) 75%);
    font-family: "Montserrat", sans-serif;
    position: relative;
  }
  .card {
    position: absolute;
    width: 560px;
    height: 320px;
    border-radius: 22px;
    box-shadow: 0 10px 24px rgba(0,0,0,0.28);
  }
  .card-front {
    left: 80px; top: 90px;
    background: var(--navy);
    display: flex; flex-direction: column; align-items: center;
  }
  .brand {
    display: flex; align-items: center; gap: 14px;
    margin-top: 110px;
  }
  .brand-dot { width: 26px; height: 26px; border-radius: 50%; background: var(--teal); }
  .brand-name {
    color: var(--paper); font-weight: 500; font-size: 30px; letter-spacing: 3px;
  }
  .front-url {
    margin-top: 88px; color: var(--paper); font-size: 15px; letter-spacing: 1.5px;
  }
  .front-url .highlight { color: var(--gold); }

  .card-back {
    left: 560px; top: 500px;
    background: var(--paper);
    display: flex; align-items: center;
  }
  .back-brand {
    width: 250px; display: flex; align-items: center; justify-content: center; gap: 12px;
  }
  .back-brand .brand-dot { width: 30px; height: 30px; }
  .back-brand .brand-name { color: var(--deep-blue); font-size: 26px; letter-spacing: 2px; }
  .divider { width: 2px; height: 180px; background: var(--gold); margin-right: 30px; }
  .details { color: var(--ink); font-size: 14px; line-height: 1.45; }
  .person-name { color: var(--gold); font-weight: 600; font-size: 22px; letter-spacing: 1px; line-height: 1.1; }
  .person-role { font-size: 15px; margin-bottom: 10px; }
  .address { margin-bottom: 10px; }
  .contact-list { list-style: none; }
  .contact-list li { display: flex; align-items: center; gap: 10px; }
  .contact-list svg { width: 12px; height: 12px; flex: none; }
  .square-mark { width: 11px; height: 11px; background: var(--gold); flex: none; }
</style>
</head>
<body>
  <section class="card card-front">
    <div class="brand">
      <span class="brand-dot"></span>
      <span class="brand-name">VERANTIS</span>
    </div>
    <p class="front-url">www.<span class="highlight">verantis</span>.com</p>
  </section>

  <section class="card card-back">
    <div class="back-brand">
      <span class="brand-dot"></span>
      <span class="brand-name">VERANTIS</span>
    </div>
    <div class="divider"></div>
    <div class="details">
      <p class="person-name">DANIEL HARTLEY</p>
      <p class="person-role">Director</p>
      <p class="address">48 Aldwyn Street<br>Kensington London W8 4QT</p>
      <ul class="contact-list">
        <li>
          <svg viewBox="0 0 12 12"><path d="M3 1 L5 3.5 L4 5 Q5 7 7 8 L8.5 7 L11 9 L9.5 11 Q4 10.5 1 3 Z" fill="var(--gold)"/></svg>
          +330 1735-4621
        </li>
        <li>
          <svg viewBox="0 0 12 12"><rect x="1" y="2.5" width="10" height="7" fill="none" stroke="var(--gold)" stroke-width="1.2"/><path d="M1 2.5 L6 6.5 L11 2.5" fill="none" stroke="var(--gold)" stroke-width="1.2"/></svg>
          info@verantis.com
        </li>
        <li>
          <svg viewBox="0 0 12 12"><circle cx="6" cy="6" r="5" fill="none" stroke="var(--gold)" stroke-width="1.1"/><ellipse cx="6" cy="6" rx="2.2" ry="5" fill="none" stroke="var(--gold)" stroke-width="1"/><path d="M1 6 H11" stroke="var(--gold)" stroke-width="1"/></svg>
          www.verantis.com
        </li>
        <li>
          <span class="square-mark"></span>
          in/verantis-4521
        </li>
      </ul>
    </div>
  </section>
</body>
</html>
```